Designs for a fundrasining event a Brown Tie Beer and Wine event

We need a flyer, brochure, and tickets for entry for a brown tie event that will be a beer and wine pairing fundraising event to be held on May 9th from 6pm to 10pm at the harborview Bistro in Cedar Lake, Indiana, USA. There will be approximately 10 silent auction items and 5 or so sponsors that we will want to have the logos of the sponsors on what we can as well, attached are the logo for Hand in Hand Foundation, IV NFP, which is the nonprofit hosting the event, there is also a logo for Mosley Counsel, LLC which is one of the sponsors (this is so you have an idea of the other 4 or so that we would also want incorporated somehow). Please ask as many questions as you may have to clarify.

Industry/Entity Type

Event

Contact Information for Business Card

Hand in Hand
Nora T. Whitfield
President/CEO
(555)382-9046
www.handinhandfdn.example

New Card:
Peter J. Whitfield
Director
(555)309-6254
www.handinhandfdn.example

New Card:
Alice M. Whitfield
Director
www.handinhandfdn.example

New Card:
Gregory B. Whitfield
Director
www.handinhandfdn.example

Font styles to use
Script

Requirements
Must have
• I want a clean card for all 4 individuals with the logo that was attached.

```html
<!DOCTYPE html>
<html lang="en">
<head>
<meta charset="utf-8">
<title>Wine and Beer Tasting – Hand in Hand Fundraiser</title>
<link rel="stylesheet" href="https://fonts.googleapis.com/css2?family=Great+Vibes&family=Tenor+Sans&family=Questrial&family=Libre+Baskerville&display=swap">
<style>
  :root {
    --bg-left: #c9dc8a;
    --bg-right: #eef4cf;
    --wine-red: #a5302b;
    --amber: #c27a2c;
    --text-orange: #c4833a;
    --ink: #3a3a30;
    --cream: #f4f1e0;
    --bow-brown: #6b4520;
    --art-top: #8e2222;
    --art-mid: #c9643a;
    --art-bottom: #e8b22c;
  }
  html, body { margin: 0; padding: 0; overflow: hidden; }
  body { width: 776px; height: 1200px; }
  .flyer {
    position: relative;
    width: 776px;
    height: 1200px;
    overflow: hidden;
    background: linear-gradient(100deg, var(--bg-left) 0%, #d9e7a6 50%, var(--bg-right) 100%);
    font-family: "Questrial", sans-serif;
  }
  .drinks-art {
    position: absolute;
    left: 540px; top: 0;
    width: 236px; height: 1200px;
    background: linear-gradient(180deg, var(--art-top) 0%, var(--art-top) 28%, var(--art-mid) 40%, var(--art-bottom) 60%, var(--art-bottom) 100%);
    opacity: 0.85;
  }
  .headline { position: absolute; margin: 0; line-height: 1; font-weight: 400; }
  .headline-wine {
    left: 40px; top: 10px;
    font-family: "Great Vibes", cursive;
    font-size: 136px; color: var(--wine-red);
  }
  .headline-and {
    left: 180px; top: 150px;
    font-family: "Great Vibes", cursive;
    font-size: 62px; color: #ffffff;
  }
  .headline-beer {
    left: 220px; top: 176px;
    font-family: "Great Vibes", cursive;
    font-size: 136px; color: var(--amber);
  }
  .headline-tasting {
    left: 72px; top: 334px;
    font-family: "Tenor Sans", sans-serif;
    font-size: 86px; letter-spacing: 2px; color: var(--wine-red);
  }
  .tagline {
    position: absolute; left: 148px; top: 432px; margin: 0;
    font-family: "Great Vibes", cursive; font-size: 46px; color: var(--text-orange);
  }
  .divider {
    position: absolute; left: 180px;
    width: 210px; height: 14px;
    border-radius: 7px;
    background: linear-gradient(90deg, transparent, var(--cream) 20%, var(--cream) 80%, transparent);
  }
  .divider-top { top: 530px; }
  .divider-bottom { top: 800px; }
  .details {
    position: absolute; left: 0; top: 582px; width: 570px;
    text-align: center; color: var(--text-orange);
    font-size: 28px; line-height: 36px;
  }
  .details p { margin: 0; }
  .details .venue { margin-top: 10px; font-variant: small-caps; font-size: 32px; letter-spacing: 1px; }
  .tickets {
    position: absolute; left: 150px; top: 830px; margin: 0;
    font-family: "Great Vibes", cursive; font-size: 50px; color: var(--wine-red);
  }
  .badge {
    position: absolute; left: 580px; top: 722px;
    width: 178px; height: 144px; border-radius: 50%;
    background: var(--cream);
    text-align: center; color: var(--wine-red);
    font-family: "Great Vibes", cursive; font-size: 38px; line-height: 1;
  }
  .badge .line-top { position: absolute; left: 0; right: 0; top: 18px; margin: 0; }
  .badge .line-bottom { position: absolute; left: 0; right: 0; top: 98px; margin: 0; }
  .badge .bow-tie {
    position: absolute; left: 61px; top: 60px;
    width: 56px; height: 30px; border-radius: 8px;
    background: var(--bow-brown);
  }
  .cause {
    position: absolute; left: 0; top: 906px; width: 570px; margin: 0;
    text-align: center; color: var(--text-orange);
    font-size: 25px; line-height: 32px;
  }
  .sponsor-row {
    position: absolute; left: 34px; display: flex; gap: 22px;
    font-family: "Libre Baskerville", serif; font-size: 12px;
    text-transform: uppercase; color: var(--ink); white-space: nowrap;
  }
  .sponsor-row-1 { top: 984px; }
  .sponsor-row-2 { top: 1030px; left: 124px; gap: 100px; }
  .sponsor { display: flex; align-items: center; gap: 7px; }
  .sponsor-mark {
    width: 20px; height: 20px; border-radius: 50%;
    border: 1.5px solid var(--ink); box-sizing: border-box; flex: none;
  }
  .host {
    position: absolute; left: 270px; top: 1078px;
    display: flex; align-items: center; gap: 8px;
    font-size: 14px; letter-spacing: 1px; text-transform: uppercase; color: var(--ink);
  }
  .host-mark { width: 28px; height: 28px; border-radius: 50%; background: var(--ink); }
  .contact {
    position: absolute; left: 0; top: 1128px; width: 620px;
    text-align: center; color: var(--wine-red);
    font-size: 15px; line-height: 22px;
  }
  .contact p { margin: 0; }
</style>
</head>
<body>
<main class="flyer">
  <div class="drinks-art" role="img" aria-label="Photo of a glass of red wine above a tall glass of beer"></div>

  <h1 class="headline headline-wine">Wine</h1>
  <span class="headline headline-and">and</span>
  <span class="headline headline-beer">Beer</span>
  <span class="headline headline-tasting">TASTING</span>
  <p class="tagline">with appetizers</p>

  <div class="divider divider-top" role="img" aria-label="Decorative flourish"></div>

  <section class="details">
    <p>Saturday, May 9, 2015</p>
    <p>6 pm to 10 pm</p>
    <p class="venue">Harborview Bistro</p>
    <p>4820 Lakeshore Ave.</p>
    <p>Cedar Lake, IN</p>
  </section>

  <div class="divider divider-bottom" role="img" aria-label="Decorative flourish"></div>

  <p class="tickets">tickets &nbsp;–&nbsp; $100</p>

  <div class="badge">
    <p class="line-top">this is a</p>
    <div class="bow-tie" role="img" aria-label="Brown bow tie illustration"></div>
    <p class="line-bottom">event</p>
  </div>

  <p class="cause">Colon Cancer Research Fund Raiser<br>sponsored by:</p>

  <div class="sponsor-row sponsor-row-1">
    <span class="sponsor"><span class="sponsor-mark"></span>Mosley Counsel, LLC</span>
    <span class="sponsor"><span class="sponsor-mark"></span>Mosley Counsel, LLC</span>
    <span class="sponsor"><span class="sponsor-mark"></span>Mosley Counsel, LLC</span>
  </div>
  <div class="sponsor-row sponsor-row-2">
    <span class="sponsor"><span class="sponsor-mark"></span>Mosley Counsel, LLC</span>
    <span class="sponsor"><span class="sponsor-mark"></span>Mosley Counsel, LLC</span>
  </div>

  <div class="host"><span class="host-mark"></span>Hand in Hand</div>

  <footer class="contact">
    <p>www.handinhandfdn.example</p>
    <p>contact Nora Whitfield 555-382-9046 or nora@handinhandfdn.example</p>
  </footer>
</main>
</body>
</html>
```